Velmor Glazing

Modern glazing company specializing in commercial fit outs, pool fencing, frameless showers and glass splash backs, im after a very young/modern logo, it doesnt have to be revelent to glazing and a classy "boss like" design for the card. thank you in advanced

im thinking carbon fiber back ground or something along that line with bright orange wording or something maybe, open to suggestions 

Fencing

company name, name, phone and products

```html
<!DOCTYPE html>
<html lang="en">
<head>
<meta charset="utf-8">
<title>Velmor Glazing – Business Card</title>
<link rel="stylesheet" href="https://fonts.googleapis.com/css2?family=Kurale&family=Varela+Round&family=Exo+2:ital,wght@1,600&display=swap">
<style>
  :root {
    --page-bg: #e9e7e3;
    --card-dark: #1c1e20;
    --card-mid: #2c2f32;
    --card-light: #3a3e41;
    --name-grey: #5a5e62;
    --band-red: #ee5a12;
    --band-orange: #f7931e;
    --band-yellow: #fbc316;
    --rule-white: #f5f5f2;
    --ink-dark: #111111;
    --text-light: #f4f4f1;
    --icon-gold: #e8c04a;
  }
  * { margin: 0; padding: 0; box-sizing: border-box; }
  html, body {
    width: 1200px;
    height: 900px;
    overflow: hidden;
    background: var(--page-bg);
  }
  .business-card {
    position: absolute;
    left: 80px;
    top: 130px;
    width: 1040px;
    height: 640px;
    overflow: hidden;
    background:
      radial-gradient(ellipse at 45% 40%, var(--card-light) 0%, var(--card-mid) 38%, var(--card-dark) 85%);
    box-shadow: 0 14px 36px rgba(0,0,0,0.28);
  }
  .holder-name {
    position: absolute;
    right: 70px;
    top: 95px;
    font-family: "Kurale", serif;
    font-size: 58px;
    color: var(--text-light);
    letter-spacing: 1px;
  }
  .company-name {
    position: absolute;
    left: 70px;
    top: 268px;
    font-family: "Varela Round", sans-serif;
    font-weight: 400;
    font-size: 80px;
    line-height: 1;
    color: var(--name-grey);
    letter-spacing: 4px;
    text-transform: uppercase;
    white-space: nowrap;
  }
  .service-bands {
    position: absolute;
    left: 0;
    top: 362px;
    width: 100%;
    height: 186px;
  }
  .service-bands .rule {
    position: absolute;
    left: 0; width: 100%;
    height: 6px;
    background: var(--rule-white);
  }
  .rule-top { top: 0; }
  .rule-bottom { bottom: 0; }
  .band {
    position: absolute;
    left: 0; width: 100%;
  }
  .band-red { top: 6px; height: 66px; background: var(--band-red); }
  .band-orange { top: 72px; height: 52px; background: var(--band-orange); }
  .band-yellow { top: 124px; height: 56px; background: var(--band-yellow); }
  .band-accents {
    position: absolute;
    right: 0;
    top: 6px;
    width: 420px;
    height: 174px;
  }
  .service-list {
    position: absolute;
    left: 120px;
    top: 6px;
    list-style: none;
    font-family: "Varela Round", sans-serif;
    font-size: 28px;
    color: var(--ink-dark);
    letter-spacing: 1.5px;
  }
  .service-list li {
    display: flex;
    align-items: center;
  }
  .service-list li:nth-child(1) { height: 66px; }
  .service-list li:nth-child(2) { height: 52px; }
  .service-list li:nth-child(3) { height: 56px; }
  .service-list .tick {
    width: 38px;
    height: 32px;
    margin-right: 22px;
    flex: none;
  }
  .contact-phone {
    position: absolute;
    right: 110px;
    top: 566px;
    display: flex;
    align-items: center;
    gap: 16px;
    font-family: "Exo 2", sans-serif;
    font-style: italic;
    font-weight: 600;
    font-size: 38px;
    color: var(--text-light);
    letter-spacing: 2px;
  }
  .contact-phone svg { width: 46px; height: 38px; }
</style>
</head>
<body>
  <div class="business-card">
    <div class="holder-name">Dane Whitlock</div>
    <div class="company-name">Velmor Glazing</div>

    <div class="service-bands">
      <div class="rule rule-top"></div>
      <div class="band band-red"></div>
      <div class="band band-orange"></div>
      <div class="band band-yellow"></div>
      <div class="rule rule-bottom"></div>

      <svg class="band-accents" viewBox="0 0 420 174" preserveAspectRatio="none" aria-hidden="true">
        <polygon points="60,110 150,110 230,174 140,174" fill="#d9a21a" opacity="0.55"/>
        <polygon points="170,110 250,110 330,174 250,174" fill="#d9a21a" opacity="0.55"/>
        <polygon points="270,110 350,110 420,168 420,174 350,174" fill="#d9a21a" opacity="0.55"/>
      </svg>

      <ul class="service-list">
        <li>
          <svg class="tick" viewBox="0 0 38 32" aria-hidden="true">
            <rect x="2" y="8" width="22" height="22" fill="none" stroke="#111" stroke-width="3"/>
            <path d="M7 17 L14 24 L34 3" fill="none" stroke="#111" stroke-width="5" stroke-linecap="round" stroke-linejoin="round"/>
          </svg>
          Pool fencing
        </li>
        <li>
          <svg class="tick" viewBox="0 0 38 32" aria-hidden="true">
            <rect x="2" y="8" width="22" height="22" fill="none" stroke="#111" stroke-width="3"/>
            <path d="M7 17 L14 24 L34 3" fill="none" stroke="#111" stroke-width="5" stroke-linecap="round" stroke-linejoin="round"/>
          </svg>
          Frameless showers
        </li>
        <li>
          <svg class="tick" viewBox="0 0 38 32" aria-hidden="true">
            <rect x="2" y="8" width="22" height="22" fill="none" stroke="#111" stroke-width="3"/>
            <path d="M7 17 L14 24 L34 3" fill="none" stroke="#111" stroke-width="5" stroke-linecap="round" stroke-linejoin="round"/>
          </svg>
          Glass splash backs
        </li>
      </ul>
    </div>

    <div class="contact-phone">
      <svg viewBox="0 0 46 38" aria-label="Phone">
        <path d="M3 12 C3 4 43 4 43 12 L43 16 L33 16 L33 11 L13 11 L13 16 L3 16 Z" fill="var(--icon-gold)"/>
        <path d="M14 15 L32 15 L40 34 L6 34 Z" fill="var(--icon-gold)"/>
        <circle cx="23" cy="25" r="5.5" fill="var(--card-mid)"/>
      </svg>
      <span>0491 572 306</span>
    </div>
  </div>
</body>
</html>
```